The most modern business card ever !!!

Our company call “Vantilo”. Vantilo is a technology company specialized in cruises solutions. Out main product is a platform to reserve cruises. This is a revolutionary platform that make easier to travel agencies and final users to reserve cruises across dozen companies like tarvik, welbi, dpv, hbt, etc..We are a “start up”, with a young team of developers and we want to transmit it.. For it, we want something different, a modern business card that represent cruises and technology.. When someone receive this card, this person should say: wowww this is different… this is modern… this is a cruise related company..
Contact Information for Business Card
Requirements
Must have
- diferent, modern
Should not have
- traditions business card

```html
<!DOCTYPE html>
<html lang="en">
<head>
<meta charset="utf-8">
<title>Vantilo Business Card</title>
<link rel="stylesheet" href="https://fonts.googleapis.com/css2?family=Montserrat:wght@600;800&family=Lustria&display=swap">
<style>
  :root {
    --stage: #2b2b2b;
    --card: #1d1d1d;
    --card-edge: #161616;
    --accent: #1f9ddb;
    --ink: #ffffff;
    --logo-muted: #8a8a8a;
    --sans: "Montserrat", Arial, sans-serif;
    --serif: "Lustria", Georgia, serif;
  }
  * { margin: 0; padding: 0; box-sizing: border-box; }
  html, body { width: 1200px; height: 895px; overflow: hidden; }
  body { background: var(--stage); position: relative; }

  .card {
    position: absolute;
    width: 560px;
    height: 320px;
    background: var(--card);
    box-shadow: 0 14px 30px rgba(0,0,0,.55);
    overflow: hidden;
  }
  .card::after {
    content: "";
    position: absolute;
    left: 0; right: 0; bottom: 0;
    height: 7px;
    background: var(--accent);
  }
  .card-front { left: 80px; top: 90px; }
  .card-back { left: 560px; top: 480px; }

  .brand-name {
    font-family: var(--sans);
    font-weight: 600;
    letter-spacing: 2px;
  }
  .card-front .brand-name {
    position: absolute;
    left: 0; right: 0; top: 112px;
    text-align: center;
    font-size: 62px;
    color: var(--logo-muted);
  }

  .card-back .brand-name {
    position: absolute;
    left: 40px; top: 128px;
    font-size: 44px;
    color: var(--ink);
  }
  .divider {
    position: absolute;
    left: 292px; top: 58px;
    width: 2px; height: 170px;
    background: var(--ink);
  }
  .contact {
    position: absolute;
    left: 318px; top: 50px;
    color: var(--ink);
    font-family: var(--serif);
    font-size: 14px;
    line-height: 1.45;
  }
  .person {
    font-family: var(--sans);
    font-weight: 800;
    font-variant: small-caps;
    font-size: 21px;
    color: var(--accent);
    line-height: 1.1;
  }
  .role { margin-bottom: 16px; }
  .address { margin-bottom: 12px; }
  .line { display: flex; align-items: center; gap: 10px; }
  .line svg { width: 14px; height: 14px; flex: none; }
</style>
</head>
<body>
  <section class="card card-front" aria-label="Card front">
    <div class="brand-name">vantilo</div>
  </section>

  <section class="card card-back" aria-label="Card back">
    <div class="brand-name">vantilo</div>
    <div class="divider"></div>
    <div class="contact">
      <div class="person">Alex Morrow</div>
      <div class="role">Founder</div>
      <div class="address">48 Harbour Lane, Suite# B<br>Bristol, UK 200B41</div>
      <div class="line">
        <svg viewBox="0 0 14 14" fill="none" stroke="#1f9ddb" stroke-width="1.4"><rect x="3.5" y="1" width="7" height="12" rx="1.2"/><line x1="6" y1="11" x2="8" y2="11"/></svg>
        <span>000 000 0000</span>
      </div>
      <div class="line">
        <svg viewBox="0 0 14 14" fill="none" stroke="#1f9ddb" stroke-width="1.4"><rect x="1" y="3" width="12" height="8"/><polyline points="1,3 7,8 13,3"/></svg>
        <span>info@vantilo.com</span>
      </div>
      <div class="line">
        <svg viewBox="0 0 14 14" fill="none" stroke="#1f9ddb" stroke-width="1.4"><circle cx="7" cy="6" r="4.5"/><line x1="4" y1="9.5" x2="2" y2="13"/></svg>
        <span>www.vantilo.com</span>
      </div>
    </div>
  </section>
</body>
</html>
```